Modern and Brightwell Car Wash Website

In Summary: A website using our Menus for Exterior and Full Service Car Washes: Meadowlark, tidewater car wash, Vireo and Copperleaf Express Car Wash websites (link attached below are good references for the type of cartoony fun design).

I will add our flyer, and menus, and some other graphics as a visual reference. Will over time add the files (AI and SVG so you can use them).

Car wash front page should be nice and clean. I have lots of videos and photos we can use throughout the wash. Would like a video on the landing page.

Our shop section can remain blank as my POS developers will create a hyperlink to it.

Main easy to use functions should be the Car Wash services, their price and full service ones as well. Allow customers to see, book if needed etc.

Please note I have the website on PLOM.

I have attached a general pdf as well for some more info.

https://meadowlarkgleamwash.ca/
https://tidewatercarwash.ca/
https://marblecarwash.com/
https://vireowash.com/
https://plainpagebuilder.com/carwash-website-design/
https://copperleafexpresscarwash.com/

```html
<!DOCTYPE html>
<html lang="en">
<head>
<meta charset="utf-8">
<title>Brightwell Car Wash – Website Screens</title>
<link href="https://fonts.googleapis.com/css2?family=Baloo+2:wght@700;800&family=Open+Sans:wght@400;600;700&display=swap" rel="stylesheet">
<style>
:root{
  --blue:#0b5fc4;
  --blue-deep:#0a4ea6;
  --navy:#0a2a5c;
  --yellow:#ffcf1a;
  --white:#ffffff;
  --paper:#f4f6fa;
  --ink:#1b2a44;
  --muted:#6b7a93;
  --line:#d9e1ee;
}
*{box-sizing:border-box;margin:0;padding:0}
html,body{width:756px;height:1200px;overflow:hidden;background:var(--white)}
body{position:relative;font-family:"Open Sans",Arial,sans-serif;color:var(--ink)}
.screen{position:absolute;top:0;overflow:hidden;display:flex;flex-direction:column;background:var(--white);box-shadow:0 0 0 1px var(--line)}
.screen--desk{width:290px;height:1200px}
.screen--a{left:14px}
.screen--b{left:318px}
.screen--mob{left:624px;width:78px;height:1200px}

.display{font-family:"Baloo 2","Trebuchet MS",sans-serif;font-weight:800;line-height:1;text-transform:uppercase}
.btn{display:inline-block;background:var(--yellow);color:var(--navy);font-weight:700;border-radius:8px;font-size:4.5px;padding:2px 6px;white-space:nowrap}

/* hero */
.hero{background:var(--blue);height:210px;position:relative;padding:8px 10px}
.nav{display:flex;align-items:center;justify-content:space-between;height:20px}
.brand{display:flex;align-items:center;gap:3px;color:var(--yellow);font-family:"Baloo 2",sans-serif;font-weight:800;font-size:8px;white-space:nowrap}
.brand i{width:7px;height:7px;border-radius:50%;background:var(--yellow);display:block;flex:none}
.nav-links{display:flex;gap:6px;font-size:4px;color:var(--white)}
.hero-copy{position:absolute;left:12px;top:52px;width:118px;color:var(--white)}
.hero-copy h1{font-size:15px;color:var(--white)}
.hero-copy h1 span{color:var(--yellow)}
.hero-copy p{font-size:4.5px;margin:6px 0 7px;line-height:1.4}
.hero-media{position:absolute;right:10px;top:30px;width:140px;height:150px;border-radius:10px;background:linear-gradient(150deg,#6fa9e6,#214f8f 60%,#f0c23a)}

/* packages */
.packages{padding:14px 18px;height:405px;background:var(--white)}
.section-title{text-align:center;font-size:11px;color:var(--blue-deep);margin-bottom:10px}
.section-kicker{text-align:center;font-size:4px;color:var(--muted);margin-bottom:2px}
.pack-grid{display:grid;grid-template-columns:1fr 1fr;gap:9px}
.pack{border-radius:8px;padding:7px;height:108px;border:1px solid var(--line);position:relative}
.pack--blue{background:var(--blue);border-color:var(--blue);color:var(--white)}
.pack h3{font-size:6px;color:var(--blue-deep);margin-bottom:4px}
.pack--blue h3{color:var(--white)}
.pack h3 b{color:var(--yellow)}
.pack ul{list-style:none;font-size:3.8px;line-height:1.7}
.pack li::before{content:"";display:inline-block;width:3px;height:3px;border-radius:50%;background:var(--blue);margin-right:3px}
.pack--blue li::before{background:var(--yellow)}
.pack .btn{position:absolute;left:7px;bottom:7px}

/* shop */
.shop{background:var(--blue);height:160px;padding:14px 20px;text-align:center;color:var(--white)}
.shop .section-title{color:var(--white)}
.shop p{font-size:4px;margin:-6px auto 8px;width:150px;line-height:1.4}
.shop-row{display:flex;gap:8px;justify-content:center;margin-bottom:8px}
.product{background:var(--white);border-radius:6px;width:62px;height:54px;padding:4px;display:flex;gap:3px;color:var(--ink)}
.product-img{width:22px;flex:none;background:linear-gradient(#ffe27a,#f2b705);border-radius:4px}
.product span{font-size:3.8px;text-align:left;line-height:1.4}

/* reviews */
.reviews{height:150px;padding:16px 18px;background:var(--paper)}
.review-row{display:flex;gap:7px}
.review{flex:1;background:var(--white);border-radius:6px;padding:6px;height:60px;box-shadow:0 1px 3px rgba(10,42,92,.12)}
.stars{color:var(--yellow);font-size:6px;letter-spacing:1px}
.review p{font-size:3.6px;line-height:1.5;color:var(--muted);margin-top:3px}
.review b{display:block;font-size:4px;margin-top:3px;color:var(--ink)}

/* cta */
.cta{height:200px;background:var(--blue);position:relative;color:var(--white)}
.cta-truck{position:absolute;left:8px;top:30px;width:110px;height:140px;border-radius:10px;background:linear-gradient(160deg,#e9eef5,#9aa9bd)}
.cta-copy{position:absolute;left:130px;top:46px;width:100px}
.cta-copy h2{font-size:12px}
.cta-copy p{font-size:4px;margin:5px 0 6px;line-height:1.4}
.cta-form{background:var(--white);border-radius:5px;padding:5px;width:92px}
.cta-form div{height:6px;border:1px solid var(--line);border-radius:3px;margin-bottom:3px}
.cta-taxi{position:absolute;right:6px;bottom:14px;width:58px;height:46px;border-radius:10px;background:linear-gradient(#ffd84a,#e0a800)}

/* footer */
.footer{flex:1;background:var(--navy);color:var(--white);padding:10px 14px;display:flex;gap:12px;font-size:3.8px;line-height:1.7}
.footer .brand{font-size:7px}
.footer h4{font-size:4.5px;color:var(--yellow)}

/* mobile */
.m-hero{background:var(--blue);height:150px;padding:6px;color:var(--white)}
.m-hero .brand{font-size:5px}
.m-hero .brand i{width:5px;height:5px}
.m-hero h1{font-size:7px;margin:8px 0 3px}
.m-hero h1 span{color:var(--yellow)}
.m-hero p{font-size:3px;line-height:1.4;margin-bottom:4px}
.m-media{height:50px;border-radius:5px;margin-top:6px;background:linear-gradient(150deg,#6fa9e6,#214f8f)}
.m-sec{padding:8px 6px}
.m-sec .section-title{font-size:6px;margin-bottom:5px}
.m-card{height:44px;border-radius:5px;margin-bottom:5px;border:1px solid var(--line);padding:4px;font-size:3px}
.m-card h3{font-size:3.6px;color:var(--blue-deep)}
.m-card--blue{background:var(--blue);color:var(--white);border-color:var(--blue)}
.m-card--blue h3{color:var(--white)}
.m-shop{background:var(--blue);padding:8px 6px;color:var(--white)}
.m-shop .section-title{color:var(--white);font-size:6px;margin-bottom:5px}
.m-prod{background:var(--white);height:30px;border-radius:4px;margin-bottom:4px;display:flex;gap:2px;padding:3px;color:var(--ink);font-size:3px}
.m-prod i{width:12px;flex:none;background:linear-gradient(#ffe27a,#f2b705);border-radius:2px}
.m-cta{background:var(--blue);padding:8px 6px;color:var(--white)}
.m-cta h2{font-size:6px;margin:4px 0}
.m-truck{height:46px;border-radius:5px;background:linear-gradient(160deg,#e9eef5,#9aa9bd)}
.m-form{background:var(--white);height:40px;border-radius:4px;margin-top:4px}
.m-footer{flex:1;background:var(--navy);padding:6px;color:var(--white);font-size:3px;line-height:1.6}
.m-footer .brand{font-size:6px}
</style>
</head>
<body>

<!-- Desktop screen A -->
<section class="screen screen--desk screen--a">
  <header class="hero">
    <nav class="nav">
      <div class="brand"><i></i>Brightwell</div>
      <div class="nav-links"><span>Home</span><span>Services</span><span>Memberships</span><span>Shop</span><span>Contact</span></div>
      <span class="btn">Book Now</span>
    </nav>
    <div class="hero-copy">
      <h1 class="display">Shine brighter <span>with Brightwell?</span></h1>
      <p>Fast exterior and full service washes that leave your car sparkling every single visit.</p>
      <span class="btn">View Packages</span>
    </div>
    <div class="hero-media" role="img" aria-label="Car moving through a wash tunnel with brushes and foam"></div>
  </header>
  <section class="packages">
    <div class="section-kicker">Our Menu</div>
    <h2 class="section-title display">Featured Packages</h2>
    <div class="pack-grid">
      <article class="pack"><h3 class="display">Exterior Clean <b>$15</b></h3><ul><li>Soft touch wash</li><li>Spot free rinse</li><li>Power dry</li><li>Wheel clean</li><li>Tire shine</li></ul><span class="btn">Buy Now</span></article>
      <article class="pack"><h3 class="display">Exterior Clean Plus <b>$22</b></h3><ul><li>Everything in clean</li><li>Triple foam polish</li><li>Underbody flush</li><li>Rain repel</li><li>Ceramic seal</li></ul><span class="btn">Buy Now</span></article>
      <article class="pack pack--blue"><h3 class="display">Everything Wash <b>$29</b></h3><ul><li>Hot wax finish</li><li>Ceramic shield</li><li>Interior vacuum</li><li>Windows cleaned</li></ul><span class="btn">Buy Now</span></article>
      <article class="pack pack--blue"><h3 class="display">Ultimate Shine <b>$39</b></h3><ul><li>Full hand dry</li><li>Dash wipe down</li><li>Mats shampooed</li><li>Air freshener</li></ul><span class="btn">Buy Now</span></article>
      <article class="pack pack--blue"><h3 class="display">Full Service <b>$49</b></h3><ul><li>Inside and out</li><li>Door jambs wiped</li><li>Leather care</li></ul><span class="btn">Buy Now</span></article>
      <article class="pack pack--blue"><h3 class="display">Unlimited Club <b>$59</b></h3><ul><li>Wash every day</li><li>Members lane</li><li>Cancel anytime</li></ul><span class="btn">Join Now</span></article>
    </div>
  </section>
  <section class="shop">
    <h2 class="section-title display">Shop Brightwell Car Wash</h2>
    <p>Gift cards, wash books and memberships available online.</p>
    <div class="shop-row">
      <div class="product"><div class="product-img" role="img" aria-label="Gift card"></div><span><b>Gift Card</b><br>Any amount</span></div>
      <div class="product"><div class="product-img" role="img" aria-label="Wash book"></div><span><b>Wash Book</b><br>Five washes</span></div>
      <div class="product"><div class="product-img" role="img" aria-label="Membership card"></div><span><b>Membership</b><br>Monthly plan</span></div>
    </div>
    <span class="btn">Visit Shop</span>
  </section>
  <section class="reviews">
    <h2 class="section-title display">What our customers say</h2>
    <div class="review-row">
      <div class="review"><div class="stars">★★★★★</div><p>Quick, friendly and my truck has never looked better.</p><b>Jordan K.</b></div>
      <div class="review"><div class="stars">★★★★★</div><p>The membership pays for itself. Great staff every time.</p><b>Priya S.</b></div>
      <div class="review"><div class="stars">★★★★★</div><p>Spotless finish and the interior smelled fresh.</p><b>Marc D.</b></div>
    </div>
  </section>
  <section class="cta">
    <div class="cta-truck" role="img" aria-label="White pickup truck covered in soap bubbles"></div>
    <div class="cta-copy">
      <h2 class="display">Ready for a shine?</h2>
      <p>Book your wash today and drive away gleaming.</p>
      <div class="cta-form"><div></div><div></div><div></div><span class="btn">Send</span></div>
    </div>
    <div class="cta-taxi" role="img" aria-label="Cartoon yellow car"></div>
  </section>
  <footer class="footer">
    <div><div class="brand"><i></i>Brightwell</div>Open daily 8am to 8pm</div>
    <div><h4>Services</h4>Exterior<br>Full Service</div>
    <div><h4>Company</h4>About<br>Careers</div>
    <div><h4>Contact</h4>(555) 014-2280<br>hello@brightwell.ca</div>
  </footer>
</section>

<!-- Desktop screen B -->
<section class="screen screen--desk screen--b">
  <header class="hero">
    <nav class="nav">
      <div class="brand"><i></i>Brightwell</div>
      <div class="nav-links"><span>Home</span><span>Services</span><span>Memberships</span><span>Shop</span><span>Contact</span></div>
      <span class="btn">Book Now</span>
    </nav>
    <div class="hero-copy">
      <h1 class="display">Shine brighter <span>with Brightwell?</span></h1>
      <p>Fast exterior and full service washes that leave your car sparkling every single visit.</p>
      <span class="btn">View Packages</span>
    </div>
    <div class="hero-media" role="img" aria-label="Car moving through a wash tunnel with brushes and foam"></div>
  </header>
  <section class="packages">
    <div class="section-kicker">Our Menu</div>
    <h2 class="section-title display">Featured Packages</h2>
    <div class="pack-grid">
      <article class="pack"><h3 class="display">Exterior Clean <b>$15</b></h3><ul><li>Soft touch wash</li><li>Spot free rinse</li><li>Power dry</li><li>Wheel clean</li><li>Tire shine</li></ul><span class="btn">Buy Now</span></article>
      <article class="pack"><h3 class="display">Exterior Clean Plus <b>$22</b></h3><ul><li>Everything in clean</li><li>Triple foam polish</li><li>Underbody flush</li><li>Rain repel</li><li>Ceramic seal</li></ul><span class="btn">Buy Now</span></article>
      <article class="pack pack--blue"><h3 class="display">Everything Wash <b>$29</b></h3><ul><li>Hot wax finish</li><li>Ceramic shield</li><li>Interior vacuum</li><li>Windows cleaned</li></ul><span class="btn">Buy Now</span></article>
      <article class="pack pack--blue"><h3 class="display">Ultimate Shine <b>$39</b></h3><ul><li>Full hand dry</li><li>Dash wipe down</li><li>Mats shampooed</li><li>Air freshener</li></ul><span class="btn">Buy Now</span></article>
      <article class="pack pack--blue"><h3 class="display">Full Service <b>$49</b></h3><ul><li>Inside and out</li><li>Door jambs wiped</li><li>Leather care</li></ul><span class="btn">Buy Now</span></article>
      <article class="pack pack--blue"><h3 class="display">Unlimited Club <b>$59</b></h3><ul><li>Wash every day</li><li>Members lane</li><li>Cancel anytime</li></ul><span class="btn">Join Now</span></article>
    </div>
  </section>
  <section class="shop">
    <h2 class="section-title display">Shop Brightwell Car Wash</h2>
    <p>Gift cards, wash books and memberships available online.</p>
    <div class="shop-row">
      <div class="product"><div class="product-img" role="img" aria-label="Gift card"></div><span><b>Gift Card</b><br>Any amount</span></div>
      <div class="product"><div class="product-img" role="img" aria-label="Wash book"></div><span><b>Wash Book</b><br>Five washes</span></div>
      <div class="product"><div class="product-img" role="img" aria-label="Membership card"></div><span><b>Membership</b><br>Monthly plan</span></div>
    </div>
    <span class="btn">Visit Shop</span>
  </section>
  <section class="reviews">
    <h2 class="section-title display">What our customers say</h2>
    <div class="review-row">
      <div class="review"><div class="stars">★★★★★</div><p>Quick, friendly and my truck has never looked better.</p><b>Jordan K.</b></div>
      <div class="review"><div class="stars">★★★★★</div><p>The membership pays for itself. Great staff every time.</p><b>Priya S.</b></div>
      <div class="review"><div class="stars">★★★★★</div><p>Spotless finish and the interior smelled fresh.</p><b>Marc D.</b></div>
    </div>
  </section>
  <section class="cta">
    <div class="cta-truck" role="img" aria-label="White pickup truck covered in soap bubbles"></div>
    <div class="cta-copy">
      <h2 class="display">Ready for a shine?</h2>
      <p>Book your wash today and drive away gleaming.</p>
      <div class="cta-form"><div></div><div></div><div></div><span class="btn">Send</span></div>
    </div>
    <div class="cta-taxi" role="img" aria-label="Cartoon yellow car"></div>
  </section>
  <footer class="footer">
    <div><div class="brand"><i></i>Brightwell</div>Open daily 8am to 8pm</div>
    <div><h4>Services</h4>Exterior<br>Full Service</div>
    <div><h4>Company</h4>About<br>Careers</div>
    <div><h4>Contact</h4>(555) 014-2280<br>hello@brightwell.ca</div>
  </footer>
</section>

<!-- Mobile screen -->
<section class="screen screen--mob">
  <header class="m-hero">
    <div class="brand"><i></i>Brightwell</div>
    <h1 class="display">Shine brighter <span>with Brightwell?</span></h1>
    <p>Fast washes that leave your car sparkling.</p>
    <span class="btn">View Packages</span>
    <div class="m-media" role="img" aria-label="Car in wash tunnel"></div>
  </header>
  <section class="m-sec">
    <h2 class="section-title display">Featured Packages</h2>
    <div class="m-card"><h3>Exterior Clean $15</h3>Wash, rinse, dry</div>
    <div class="m-card"><h3>Clean Plus $22</h3>Foam and seal</div>
    <div class="m-card m-card--blue"><h3>Everything $29</h3>Wax and vacuum</div>
    <div class="m-card m-card--blue"><h3>Ultimate $39</h3>Full hand dry</div>
    <div class="m-card m-card--blue"><h3>Full Service $49</h3>Inside and out</div>
  </section>
  <section class="m-shop">
    <h2 class="section-title display">Shop Brightwell Car Wash</h2>
    <div class="m-prod"><i role="img" aria-label="Gift card"></i>Gift Card</div>
    <div class="m-prod"><i role="img" aria-label="Wash book"></i>Wash Book</div>
    <div class="m-prod"><i role="img" aria-label="Membership card"></i>Membership</div>
  </section>
  <section class="m-sec">
    <h2 class="section-title display">What our customers say</h2>
    <div class="m-card"><span class="stars">★★★★★</span><br>Quick and friendly.</div>
  </section>
  <section class="m-cta">
    <div class="m-truck" role="img" aria-label="White pickup truck with soap bubbles"></div>
    <h2 class="display">Ready for a shine?</h2>
    <div class="m-form"></div>
  </section>
  <footer class="m-footer"><div class="brand"><i></i>Brightwell</div>Open daily 8am to 8pm</footer>
</section>

</body>
</html>
```